Ledgerway Partners, LLC
Project: Biz Card & Stationery
Biz Card & Stationery - Consulting
Biz Card & Stationery
Professional
Denise M. Holloway, CPP, PMP
Founder and CEO
4812 Linwood Avenue NE Suite 210 Atlanta, GA 30318
dholloway@ledgerway-hq.com
ledgerway-hq.com
DUNS No. 052817634 NAICS CODES: 541611 541214 541512 611430 561320

```html
<!DOCTYPE html>
<html lang="en">
<head>
<meta charset="utf-8">
<title>Ledgerway Partners, LLC — Stationery</title>
<link href="https://fonts.googleapis.com/css2?family=Open+Sans:wght@400;600;700&display=swap" rel="stylesheet">
<style>
:root{
  --canvas:#ffffff;
  --paper:#eef2ec;
  --ink:#3b3b3b;
  --muted:#8a8f88;
  --red:#d7222d;
  --purple:#7a3b8f;
  --mark:rgba(190,200,188,.45);
  --edge:#d9ddd6;
}
*{box-sizing:border-box;margin:0;padding:0}
html,body{width:1200px;height:240px;overflow:hidden;background:var(--canvas);font-family:"Open Sans",sans-serif;color:var(--ink)}
.sheet{position:absolute;background:var(--paper);border:1px solid var(--edge);overflow:hidden}
.card{width:185px;height:103px}
.letter{width:176px;height:216px;top:12px}
.brand{position:absolute;display:flex;align-items:center;gap:3px;font-weight:700;font-size:7px;color:var(--red);white-space:nowrap}
.brand .dot{width:7px;height:7px;border-radius:50%;background:var(--red)}
.mark{position:absolute;border-radius:50%;background:var(--mark);display:flex;align-items:center;justify-content:center;text-align:center;font-weight:700;color:rgba(255,255,255,.8);line-height:1.1}
.name{font-weight:700;font-size:7px;white-space:nowrap}
.title{font-size:5px;color:var(--muted)}
.phones{font-size:4.5px;line-height:1.5;color:var(--ink)}
.foot{position:absolute;left:0;right:0;bottom:0;height:14px;border-top:1.5px solid var(--red);font-size:3.8px;color:var(--muted);display:flex;justify-content:space-between;align-items:center;padding:0 6px}
.flap{position:absolute;left:0;right:0;top:0;height:22px}
.flap.red{background:var(--red)}
.flap.purple{background:var(--purple)}
</style>
</head>
<body>

<!-- column 1 -->
<div class="sheet card" style="left:12px;top:12px">
  <div class="brand" style="left:7px;top:7px"><span class="dot"></span>Ledgerway Partners, LLC</div>
</div>
<div class="sheet card" style="left:12px;top:125px">
  <div style="position:absolute;left:8px;top:14px">
    <div class="name">Denise M. Holloway, CPP, PMP</div>
    <div class="title">Founder and CEO</div>
  </div>
  <div class="phones" style="position:absolute;left:84px;top:38px">T 404.555.0142<br>M 404.555.0178<br>F 404.555.0190</div>
  <div class="foot"><span>ledgerway-hq.com</span><span>4812 Linwood Avenue NE Suite 210 Atlanta, GA 30318</span></div>
</div>

<!-- column 2 -->
<div class="sheet card" style="left:209px;top:12px">
  <div class="mark" style="left:60px;top:14px;width:64px;height:64px;font-size:6px">Ledgerway<br>Partners</div>
</div>
<div class="sheet card" style="left:209px;top:125px">
  <div class="mark" style="left:66px;top:10px;width:56px;height:56px;font-size:5px">Ledgerway<br>Partners</div>
  <div style="position:absolute;left:8px;top:36px">
    <div class="name">Denise M. Holloway, CPP, PMP</div>
    <div class="title">Founder and CEO</div>
  </div>
  <div class="phones" style="position:absolute;left:116px;top:58px">T 404.555.0142</div>
  <div class="foot"><span>dholloway@ledgerway-hq.com</span><span>Atlanta, GA 30318</span></div>
</div>

<!-- column 3 -->
<div class="sheet card" style="left:405px;top:12px">
  <div class="mark" style="left:60px;top:8px;width:64px;height:64px;font-size:6px">Ledgerway<br>Partners</div>
  <div style="position:absolute;left:8px;top:76px">
    <div class="name" style="font-size:5.5px">Denise M. Holloway, CPP, PMP</div>
    <div class="title">Founder and CEO</div>
  </div>
</div>
<div class="sheet card" style="left:405px;top:125px">
  <div class="mark" style="left:60px;top:10px;width:64px;height:64px;font-size:6px">Ledgerway<br>Partners</div>
  <div class="foot"><span>ledgerway-hq.com</span><span>DUNS No. 052817634</span></div>
</div>

<!-- envelopes -->
<div class="sheet card" style="left:612px;top:12px">
  <div class="flap red"></div>
  <div class="mark" style="left:70px;top:26px;width:44px;height:44px;font-size:4.5px">Ledgerway<br>Partners</div>
</div>
<div class="sheet card" style="left:612px;top:125px">
  <div class="flap purple"></div>
  <div class="mark" style="left:70px;top:26px;width:44px;height:44px;font-size:4.5px">Ledgerway<br>Partners</div>
</div>

<!-- letterhead 1 -->
<div class="sheet letter" style="left:808px">
  <div class="brand" style="left:8px;top:9px"><span class="dot"></span>Ledgerway Partners, LLC</div>
  <div class="mark" style="left:30px;top:72px;width:90px;height:90px;font-size:8px">Ledgerway<br>Partners</div>
  <div class="foot"><span>ledgerway-hq.com</span><span>4812 Linwood Avenue NE Suite 210 Atlanta, GA 30318</span></div>
</div>

<!-- letterhead 2 -->
<div class="sheet letter" style="left:1008px">
  <div style="position:absolute;right:8px;top:9px;text-align:right">
    <div class="name" style="font-size:5.5px">Denise M. Holloway, CPP, PMP</div>
    <div class="title">Founder and CEO</div>
  </div>
  <div class="mark" style="left:28px;top:60px;width:110px;height:110px;font-size:9px">Ledgerway<br>Partners</div>
  <div class="foot"><span>dholloway@ledgerway-hq.com</span><span>NAICS: 541611 541214 541512</span></div>
</div>

</body>
</html>
```